Aerial photo/video drone company needs new business card

Aerial visual company who offers photos and video services via drones.

We are QVL certified and work in the real estate, insurance, construction, and film industries.

I'm looking for a clean, professional, maybe even edgy design, that will be a conversation starter when networking.

I've included our logo, current business card, and font.

Our current business card is decent; albeit, I'm looking for something more unique. If you folks provide good designs, I'll definitely guarantee payment (and I'm not opposed to tipping if the design is above and beyond).

Target Market(s)

Insurance companies, real estate agents, construction companies, advertising & other creative agencies, and filmmakers/producers.

Industry/Entity Type

Business

Contact Information for Business Card

Company name pronounced air-a-vee.

Font styles to use
Other font styles liked:
• Font was uploaded; that or similar; not opposed to other fonts if they work well with the design

Requirements
Must have
• Clearly prominent logo; my name and title; phone number; email address; web address; mentioned "QVL Certified" or similar; should indicate "Aerial visual"
Nice to have
• Watermark of logo or otherwise
Should not have
• Pictures of drones or scenic shots

```html
<!DOCTYPE html>
<html lang="en">
<head>
<meta charset="utf-8">
<title>Skyvane Business Card</title>
<link rel="stylesheet" href="https://fonts.googleapis.com/css2?family=Montserrat:wght@400;500;600;700&display=swap">
<style>
  :root {
    --page: #ebebeb;
    --card-black: #1f1f21;
    --card-black-soft: #2c2c2e;
    --sky-blue: #5b9bd9;
    --slate-blue: #5a6a8c;
    --band-grey: #6a7590;
    --white: #ffffff;
    --soft-white: #d8d8d8;
  }
  * { margin: 0; padding: 0; box-sizing: border-box; }
  html, body {
    width: 1200px; height: 800px; overflow: hidden;
    background: var(--page);
    font-family: "Montserrat", sans-serif;
  }
  .sheet {
    width: 1200px; height: 800px;
    display: flex; align-items: center; justify-content: center; gap: 50px;
  }
  .card {
    position: relative;
    width: 525px; height: 300px;
    background: linear-gradient(160deg, var(--card-black-soft), var(--card-black) 60%);
    overflow: hidden;
    box-shadow: 0 10px 30px rgba(0,0,0,0.12);
  }
  .card__swoosh { position: absolute; inset: 0; width: 100%; height: 100%; }

  /* Front */
  .front__brand {
    position: absolute; left: 0; right: 0; top: 92px;
    display: flex; flex-direction: column; align-items: center;
  }
  .brand-lockup { display: flex; align-items: center; gap: 14px; }
  .brand-dot {
    width: 30px; height: 30px; border-radius: 50%;
    background: var(--slate-blue);
  }
  .brand-name {
    font-weight: 700; font-size: 66px; letter-spacing: 1px;
    color: var(--slate-blue); line-height: 1;
  }
  .front__cert {
    margin-top: 10px; font-size: 13px; font-weight: 500;
    letter-spacing: 5px; color: var(--white);
  }

  /* Back */
  .back__person {
    position: absolute; left: 190px; top: 72px;
    color: var(--white);
  }
  .person-name { font-size: 21px; font-weight: 600; letter-spacing: 1px; line-height: 1.2; }
  .person-title { font-size: 11px; font-weight: 400; margin: 3px 0 12px 34px; color: var(--soft-white); }
  .contact-list { list-style: none; font-size: 14px; font-weight: 500; color: var(--sky-blue); line-height: 1.25; }
  .back__services {
    position: absolute; left: 18px; top: 230px;
    font-size: 8.5px; font-weight: 500; color: var(--sky-blue); line-height: 1.45;
    white-space: nowrap;
  }
  .back__brand {
    position: absolute; right: 20px; top: 138px;
    display: flex; align-items: center; gap: 7px;
  }
  .back__brand .brand-dot { width: 13px; height: 13px; }
  .back__brand .brand-name { font-size: 28px; }
</style>
</head>
<body>
<main class="sheet">

  <section class="card card--front" aria-label="Card front">
    <svg class="card__swoosh" viewBox="0 0 525 300" preserveAspectRatio="none" aria-hidden="true">
      <path d="M160 300 Q330 210 525 250 L525 300 Z" fill="var(--band-grey)"/>
      <path d="M230 300 Q370 230 525 262 L525 300 Z" fill="var(--sky-blue)"/>
    </svg>
    <div class="front__brand">
      <div class="brand-lockup">
        <span class="brand-name">skyvane</span>
        <span class="brand-dot"></span>
      </div>
      <p class="front__cert">QVL CERTIFIED</p>
    </div>
  </section>

  <section class="card card--back" aria-label="Card back">
    <svg class="card__swoosh" viewBox="0 0 525 300" preserveAspectRatio="none" aria-hidden="true">
      <path d="M0 0 L300 0 Q150 15 0 60 Z" fill="var(--sky-blue)"/>
      <path d="M0 60 Q150 15 300 0 L320 0 Q160 25 0 78 Z" fill="var(--band-grey)"/>
      <path d="M290 300 Q400 232 525 232 L525 300 Z" fill="var(--band-grey)"/>
      <path d="M335 300 Q420 246 525 246 L525 300 Z" fill="var(--sky-blue)"/>
    </svg>
    <div class="back__person">
      <h1 class="person-name">DANIEL J. CORWIN</h1>
      <p class="person-title">Owner | sUAS Pilot</p>
      <ul class="contact-list">
        <li>dan@skyvane.com</li>
        <li>555.014.2288</li>
        <li>skyvane.com</li>
      </ul>
    </div>
    <p class="back__services">
      QVL Part 107 Commercial sUAS Certified<br>
      Aerial Visual for Real Estate | Insurance | Construction | Film
    </p>
    <div class="back__brand">
      <span class="brand-name">skyvane</span>
      <span class="brand-dot"></span>
    </div>
  </section>

</main>
</body>
</html>
```